Modern Stationary for Architecs
Orbit Architecs
Simple
Arch. Fahad Nabil Alqurashi
CEO
KSA
Riyadh
Alwurud -Prince Faisal Road
eng.qurashi@postvela.net
We are looking for a professional and attractive for our Stationary .
so we expect to see :
Letterhead
envelop
CD label & Jacket
Folder
Just logo
logo
Please us this file for all stationary
Please use this file in Letterhead ONLY

```html
<!DOCTYPE html>
<html lang="en">
<head>
<meta charset="utf-8">
<title>Orbit Architecs — Business Card</title>
<link rel="stylesheet" href="https://fonts.googleapis.com/css2?family=Montserrat:wght@400;600;700&family=Open+Sans:wght@400;600;700&display=swap">
<style>
  :root {
    --bg: #e4e4e4;
    --card: #ffffff;
    --red: #b3141c;
    --red-dark: #7d0b10;
    --ink: #4a4a4a;
    --grey: #8a8a8a;
    --grey-light: #c9c9c9;
  }
  * { box-sizing: border-box; margin: 0; padding: 0; }
  html, body { width: 1200px; height: 864px; overflow: hidden; }
  body {
    background: var(--bg);
    font-family: "Open Sans", sans-serif;
    display: flex;
    align-items: center;
    justify-content: center;
    gap: 40px;
  }
  .card {
    position: relative;
    width: 540px;
    height: 310px;
    background: var(--card);
    border-radius: 18px;
    overflow: hidden;
    box-shadow: 0 6px 18px rgba(0,0,0,0.18);
  }
  /* back side */
  .card-back { display: flex; flex-direction: column; align-items: center; justify-content: center; gap: 26px; }
  .brand { display: flex; align-items: center; gap: 12px; }
  .brand-dot { width: 16px; height: 16px; border-radius: 50%; background: var(--red); flex: none; }
  .brand-name {
    font-family: "Montserrat", sans-serif;
    font-weight: 600;
    color: var(--ink);
    letter-spacing: 2px;
    text-transform: uppercase;
    white-space: nowrap;
  }
  .card-back .brand-name { font-size: 34px; }
  .web {
    font-family: "Montserrat", sans-serif;
    font-size: 15px;
    font-weight: 600;
    letter-spacing: 3px;
    color: var(--ink);
  }
  .web .accent { color: var(--red); }
  /* front side */
  .card-front .brand { position: absolute; left: 34px; top: 36px; }
  .card-front .brand-name { font-size: 26px; }
  .person { position: absolute; left: 34px; top: 100px; }
  .person-name { color: var(--red); font-weight: 700; font-size: 13px; }
  .person-role { color: var(--grey); font-size: 11px; margin-top: 2px; }
  .contacts { position: absolute; left: 300px; top: 96px; list-style: none; }
  .contacts li { display: flex; align-items: center; gap: 8px; font-size: 11px; color: var(--ink); margin-bottom: 7px; white-space: nowrap; }
  .contacts svg { width: 14px; height: 14px; flex: none; }
  .address { position: absolute; left: 34px; top: 160px; font-size: 11px; font-style: normal; color: var(--ink); line-height: 1.55; }
  .base-rule { position: absolute; left: 0; right: 0; bottom: 22px; height: 2px; background: var(--grey-light); }
  .base-band { position: absolute; left: 0; right: 0; bottom: 0; height: 14px; background: var(--red); }
</style>
</head>
<body>
  <section class="card card-back">
    <div class="brand">
      <span class="brand-dot"></span>
      <span class="brand-name">Orbit Architecs</span>
    </div>
    <p class="web">www.<span class="accent">orbitarchitecs-studio</span>.com</p>
  </section>

  <section class="card card-front">
    <div class="brand">
      <span class="brand-dot"></span>
      <span class="brand-name">Orbit Architecs</span>
    </div>

    <div class="person">
      <p class="person-name">Arch. Fahad Nabil Alqurashi</p>
      <p class="person-role">CEO</p>
    </div>

    <ul class="contacts">
      <li>
        <svg viewBox="0 0 14 14"><rect width="14" height="14" rx="2" fill="var(--red)"/><path d="M4 3.5 L6 3.5 L6.6 5.6 L5.6 6.4 C6.1 7.5 6.7 8.1 7.7 8.5 L8.5 7.5 L10.5 8.1 L10.5 10 C7 10.3 3.7 7 4 3.5Z" fill="#fff"/></svg>
        +966 50 214 7730
      </li>
      <li>
        <svg viewBox="0 0 14 14"><rect width="14" height="14" rx="2" fill="var(--red)"/><rect x="4.5" y="2.5" width="5" height="9" rx="1" fill="#fff"/></svg>
        +966 50 214 7731
      </li>
      <li>
        <svg viewBox="0 0 14 14"><rect width="14" height="14" rx="2" fill="var(--red)"/><rect x="3" y="5" width="8" height="6" fill="#fff"/><rect x="4.5" y="2.5" width="5" height="3" fill="#fff"/></svg>
        +966 11 482 5590
      </li>
      <li>
        <svg viewBox="0 0 14 14"><rect width="14" height="14" rx="2" fill="var(--red)"/><rect x="3" y="4" width="8" height="6" fill="#fff"/><path d="M3 4 L7 7.5 L11 4" stroke="var(--red)" fill="none" stroke-width="1"/></svg>
        eng.qurashi@postvela.net
      </li>
    </ul>

    <address class="address">
      KSA<br>
      Riyadh<br>
      Alwurud -Prince Faisal Road
    </address>

    <div class="base-rule"></div>
    <div class="base-band"></div>
  </section>
</body>
</html>
```